디자인 카테고리
기타 (식당/카페 업종)
브랜드 소개
은빛식당은 강원도 정선군에 위치한 “청정숙성한우전문점”입니다.
웻 에이징 공법으로 쫄깃한 식감과 고소한 풍미를 제공해줍니다.
저희는 “들녘믿음소”를 사용하여 고객들이 안심하고 먹을 수 있도록 신경을 많이 써왔고
서비스면에서도 지속적으로 교육하여 같은 지역의 다른 식당과 차별화된 전략을 장점으로 내세우고 있습니다.
저희는 특별히 주문제작한 무쇠불판을 사용하여 발암물질인 “벤조피렌”의 발생량을 낮추고 맛의 수준을 한단계 높였습니다.
저희는 “한우등심”, “특수부위”, “설렁탕”을 전문으로 취급하는 음식점이지만 이 외에도 각종 맛있는 식사류가 준비되어있습니다.

```html
<!DOCTYPE html>
<html lang="ko">
<head>
<meta charset="utf-8">
<title>은빛식당 한우굽기설명서</title>
<link href="https://fonts.googleapis.com/css2?family=Noto+Sans+KR:wght@400;500;700;900&family=Nanum+Myeongjo:wght@700;800&family=Nanum+Pen+Script&display=swap" rel="stylesheet">
<style>
:root{
  --bg:#e6e2dc;
  --frame:#4b3b33;
  --paper:#efe7da;
  --paper-dark:#e4d9c8;
  --ink:#3a2e28;
  --ink-soft:#6b5d54;
  --label:#5a463b;
  --line:#b9ab98;
}
*{margin:0;padding:0;box-sizing:border-box}
html,body{width:1200px;height:1200px;overflow:hidden;background:var(--bg);font-family:"Noto Sans KR",sans-serif;color:var(--ink)}
.sheet{position:absolute;left:40px;top:156px;width:1120px;height:887px;background:var(--frame);padding:26px;display:grid;grid-template-columns:790px 263px;grid-template-rows:385px 435px;gap:15px}
.panel{background:var(--paper);border-radius:6px;position:relative}
.guide{grid-column:1;grid-row:1;padding:22px 30px}
.bottom{grid-column:1;grid-row:2;display:grid;grid-template-columns:355px 418px;gap:17px}
.menu{grid-column:2;grid-row:1/3;padding:20px 16px}
.guide-head{display:flex;justify-content:space-between;align-items:flex-end;padding-bottom:12px;border-bottom:2px dashed var(--line)}
.guide-title{font-size:32px;font-weight:900;letter-spacing:-1px}
.guide-note{font-size:11px;color:var(--ink-soft)}
.steps{display:grid;grid-template-columns:repeat(4,1fr);gap:18px;margin-top:18px}
.step-heat{display:flex;justify-content:flex-end;height:26px;padding-right:16px}
.step-pan{height:110px;margin:4px 0 16px;border-radius:10px;background:linear-gradient(180deg,#d9d6d0 0%,#a9adb2 55%,#8d9297 100%)}
.step-body{display:flex;gap:10px;align-items:flex-start}
.step-num{flex:none;width:34px;height:34px;border-radius:50%;background:var(--frame);color:var(--paper);font-weight:700;font-size:17px;display:flex;align-items:center;justify-content:center}
.step-text{font-size:12.5px;line-height:1.55}
.marble{padding:20px 18px}
.panel-title{font-family:"Nanum Myeongjo",serif;font-weight:800;font-size:22px;letter-spacing:-.5px}
.marble-top{display:flex;gap:10px;margin-top:14px}
.marble-copy{width:170px;font-size:11px;line-height:1.6;color:var(--ink-soft)}
.marble-photo{flex:1;height:112px;border-radius:8px;background:linear-gradient(135deg,#dfe9d8,#a9cf9f 60%,#c97e70)}
.tag{display:inline-block;margin:10px 0 4px;padding:2px 7px;background:var(--label);color:var(--paper);font-size:11px;font-weight:700}
.marble-warn{font-size:11px;line-height:1.6;color:var(--ink-soft)}
.points{display:grid;grid-template-columns:1fr 1fr;gap:12px;margin-top:18px}
.point{height:56px;border:2px solid var(--ink);border-radius:8px;display:flex;align-items:center;justify-content:center;text-align:center;font-size:13px;font-weight:700;line-height:1.35;background:#f6f0e6}
.pan{padding:20px 20px}
.pan-bar{margin-top:12px;background:var(--label);color:var(--paper);font-size:11.5px;font-weight:500;padding:5px 10px}
.pan-list{list-style:none;margin-top:8px;font-size:11px;line-height:1.7;color:var(--ink-soft)}
.pan-list li::before{content:"● ";color:var(--ink)}
.pan-mid{display:flex;gap:14px;margin-top:14px;align-items:center}
.pan-drawing{width:160px;height:120px;border-radius:8px;background:linear-gradient(180deg,#e8e0d2,#d6cbb9)}
.compare{flex:1;font-size:11px}
.compare-cap{font-weight:700;text-align:center;padding:4px;border-bottom:1.5px solid var(--ink)}
.compare table{width:100%;border-collapse:collapse;margin-top:4px}
.compare td{border:1px solid var(--line);padding:5px 4px;text-align:center;font-size:10.5px}
.compare .hl{background:var(--paper-dark);font-weight:700}
.pan-foot{margin-top:14px;font-size:10.5px;color:var(--ink-soft);text-align:center}
.slogan{margin-top:10px;text-align:center;font-family:"Nanum Pen Script",cursive;font-size:34px;color:var(--ink);letter-spacing:1px}
.menu-head{font-size:14px;font-weight:700;display:flex;align-items:center;gap:6px;padding-bottom:10px}
.menu-head::before{content:"";width:8px;height:8px;border-radius:50%;background:var(--ink)}
.dish{display:flex;gap:10px;align-items:center;height:154px;border-top:1.5px dashed var(--line)}
.dish-photo{flex:none;width:108px;height:96px;border-radius:10px;background:linear-gradient(180deg,var(--c),#8e9196)}
.dish-name{display:inline-block;background:var(--label);color:var(--paper);font-size:13px;font-weight:700;padding:3px 8px}
.dish-desc{margin-top:6px;font-size:10.5px;line-height:1.5;color:var(--ink-soft)}
</style>
</head>
<body>
<main class="sheet">
  <section class="panel guide">
    <header class="guide-head">
      <h1 class="guide-title">한우굽기설명서</h1>
      <p class="guide-note">※ 아래 적힌 순서대로 구워드시면 한우를 더 맛있게 드실 수 있습니다.</p>
    </header>
    <div class="steps">
      <div class="step">
        <div class="step-heat"><svg width="50" height="22" viewBox="0 0 50 22"><path d="M8 19c-4-3-2-8 1-11 0 3 2 4 3 5 1-3 0-6 3-9 1 5 4 7 2 12-1 2-3 3-5 3z" fill="var(--ink)"/><circle cx="36" cy="11" r="9" fill="none" stroke="var(--ink)" stroke-width="2"/><line x1="36" y1="11" x2="42" y2="5" stroke="var(--ink)" stroke-width="2"/></svg></div>
        <div class="step-pan" role="img" aria-label="연기가 나도록 달궈지는 무쇠불판 그림"></div>
        <div class="step-body"><span class="step-num">1</span><p class="step-text">무쇠불판에서 연기가 날 때까지 센 불로 충분히 달구어 주세요.</p></div>
      </div>
      <div class="step">
        <div class="step-heat"><svg width="50" height="22" viewBox="0 0 50 22"><path d="M8 19c-4-3-2-8 1-11 0 3 2 4 3 5 1-3 0-6 3-9 1 5 4 7 2 12-1 2-3 3-5 3z" fill="var(--ink)"/><circle cx="36" cy="11" r="9" fill="none" stroke="var(--ink)" stroke-width="2"/><line x1="36" y1="11" x2="27" y2="11" stroke="var(--ink)" stroke-width="2"/></svg></div>
        <div class="step-pan" role="img" aria-label="집게로 기름을 바르는 불판 그림"></div>
        <div class="step-body"><span class="step-num">2</span><p class="step-text">연기가 피어오르기 시작하면 불을 줄이고 기름을 넓게 펴 발라 주세요.</p></div>
      </div>
      <div class="step">
        <div class="step-heat"><svg width="50" height="22" viewBox="0 0 50 22"><path d="M8 19c-4-3-2-8 1-11 0 3 2 4 3 5 1-3 0-6 3-9 1 5 4 7 2 12-1 2-3 3-5 3z" fill="var(--ink)"/><circle cx="36" cy="11" r="9" fill="none" stroke="var(--ink)" stroke-width="2"/><line x1="36" y1="11" x2="36" y2="2" stroke="var(--ink)" stroke-width="2"/></svg></div>
        <div class="step-pan" role="img" aria-label="한우를 올려 굽는 불판 그림"></div>
        <div class="step-body"><span class="step-num">3</span><p class="step-text">불판을 중불로 낮추고 1인 2~3점씩 한우를 올려 구워 주세요.</p></div>
      </div>
      <div class="step">
        <div class="step-heat"><svg width="50" height="22" viewBox="0 0 50 22"><path d="M8 19c-4-3-2-8 1-11 0 3 2 4 3 5 1-3 0-6 3-9 1 5 4 7 2 12-1 2-3 3-5 3z" fill="var(--ink)"/><circle cx="36" cy="11" r="9" fill="none" stroke="var(--ink)" stroke-width="2"/><line x1="36" y1="11" x2="42" y2="5" stroke="var(--ink)" stroke-width="2"/></svg></div>
        <div class="step-pan" role="img" aria-label="다시 달궈지는 빈 불판 그림"></div>
        <div class="step-body"><span class="step-num">4</span><p class="step-text">다시 불을 강으로 올리고 1~3번 과정을 반복해 주세요.</p></div>
      </div>
    </div>
  </section>

  <div class="bottom">
    <section class="panel marble">
      <h2 class="panel-title">마블보다 무서운 이것은?</h2>
      <div class="marble-top">
        <p class="marble-copy">은빛식당의 특제 찍먹이와 한우를 함께 드시면 고소한 풍미와 담백한 향이 조화롭게 어우러집니다. 곁들임 채소와 함께 즐겨 보세요.</p>
        <div class="marble-photo" role="img" aria-label="파채 위에 올린 한우 한 점 그림"></div>
      </div>
      <span class="tag">주의사항</span>
      <p class="marble-warn">혹시나 불 조절을 잘못하여 불판이 탔다면 직원에게 말씀해 주시면 바로 새 불판으로 교체해 드립니다.</p>
      <div class="points">
        <div class="point">들녘믿음소 사용</div>
        <div class="point">불필요한 지방<br>사전 제거후 제공</div>
        <div class="point">400석 예약 가능</div>
        <div class="point">1+ 숙성한우전문</div>
      </div>
    </section>

    <section class="panel pan">
      <h2 class="panel-title">무쇠불판이 좋은 이유</h2>
      <p class="pan-bar">은빛식당은 소고기가 가장 맛있게 구워지는 무쇠불판을 사용합니다.</p>
      <ul class="pan-list">
        <li>무쇠불판은 육즙을 보존하여 부드럽게 구워져 고기맛이 좋습니다.</li>
        <li>온도를 오래 유지시켜주어 한결같이 맛있게 드실 수 있습니다.</li>
      </ul>
      <div class="pan-mid">
        <div class="pan-drawing" role="img" aria-label="무쇠불판 선 그림"></div>
        <div class="compare">
          <p class="compare-cap">벤조피렌(발암물질) 발생량 비교</p>
          <table>
            <tr><td>숯불구이 21㎍/kg</td><td>불판구이 6㎍/kg</td></tr>
            <tr><td class="hl" colspan="2">은빛식당 무쇠불판 0.00005㎍/kg</td></tr>
          </table>
        </div>
      </div>
      <p class="pan-foot">벤조피렌 발생량을 낮추고 맛의 수준을 한 단계 높였습니다.</p>
      <p class="slogan">은빛식당에서 맛도 즐기고 건강도 챙기세요!</p>
    </section>
  </div>

  <aside class="panel menu">
    <h2 class="menu-head">은빛식당 BEST 식사류</h2>
    <div class="dish" style="--c:#e9e4d6"><div class="dish-photo" role="img" aria-label="뚝배기에 담긴 설렁탕 그림"></div><div><span class="dish-name">설렁탕</span><p class="dish-desc">은빛식당 설렁탕은 24시간 이상 한우 사골을 우려내어 깊고 진한 국물이 일품입니다.</p></div></div>
    <div class="dish" style="--c:#dfe3cf"><div class="dish-photo" role="img" aria-label="뚝배기에 담긴 소고기무국 그림"></div><div><span class="dish-name">소고기무국</span><p class="dish-desc">깨끗한 다시와 한우양지, 제주도산 무를 넣어 맑고 시원하게 끓였습니다.</p></div></div>
    <div class="dish" style="--c:#d7877a"><div class="dish-photo" role="img" aria-label="그릇에 담긴 육회비빔밥 그림"></div><div><span class="dish-name">육회비빔밥</span><p class="dish-desc">한우 생고기와 제철 채소를 올려 고소한 참기름과 함께 비벼 드세요.</p></div></div>
    <div class="dish" style="--c:#c9805f"><div class="dish-photo" role="img" aria-label="뚝배기에 담긴 우거지해장국 그림"></div><div><span class="dish-name">우거지해장국</span><p class="dish-desc">푹 삶은 우거지와 한우 뼈 육수로 얼큰하고 든든하게 끓였습니다.</p></div></div>
    <div class="dish" style="--c:#c08a5e"><div class="dish-photo" role="img" aria-label="뚝배기에 담긴 차돌된장찌개 그림"></div><div><span class="dish-name">차돌된장찌개</span><p class="dish-desc">직접 담근 된장에 한우 차돌박이를 듬뿍 넣어 구수한 맛을 살렸습니다.</p></div></div>
  </aside>
</main>
</body>
</html>
```